Business Card Design

Need business card design for all carpentry & construction solutions. We would like to see designs that use black as a background with orange writing as it would stand out.

Business

RMP CONTRACTING
PETER LANGFORD
14 CALLOWAY ST
ELDON VALE
EV 6712
0487315962
rmpcontracting@kestrelmail.com

```html
<!DOCTYPE html>
<html lang="en">
<head>
<meta charset="utf-8">
<title>RMP Contracting – Business Card</title>
<link rel="stylesheet" href="https://fonts.googleapis.com/css2?family=Jost:wght@300;400;700&display=swap">
<style>
  :root {
    --backdrop: #e6e6e4;
    --card-black: #1b1b1b;
    --card-yellow: #f6b70f;
    --accent: #f6b70f;
    --soft-grey: #a3a3a3;
    --ink: #141414;
    --ink-soft: #3a3a3a;
  }
  * { margin: 0; padding: 0; box-sizing: border-box; }
  html, body {
    width: 1200px;
    height: 982px;
    overflow: hidden;
    background: var(--backdrop);
    font-family: "Jost", "Futura", sans-serif;
  }
  .sheet {
    position: relative;
    width: 1200px;
    height: 982px;
  }
  .card {
    position: absolute;
    left: 240px;
    width: 720px;
    height: 440px;
    border-radius: 22px;
    box-shadow: 0 10px 28px rgba(0,0,0,0.18);
  }
  .card--front { top: 34px; background: var(--card-black); }
  .card--back  { top: 508px; background: var(--card-yellow); }

  .card__email {
    position: absolute;
    left: 84px;
    top: 60px;
    font-size: 20px;
    font-weight: 300;
    letter-spacing: 0.3px;
  }
  .card__details {
    position: absolute;
    left: 84px;
    top: 200px;
  }
  .company {
    font-size: 36px;
    font-weight: 400;
    line-height: 1;
    letter-spacing: 0.5px;
  }
  .person {
    margin-top: 10px;
    font-size: 28px;
    line-height: 1.1;
  }
  .person__first { font-weight: 300; }
  .person__last { font-weight: 700; }
  .address {
    margin-top: 12px;
    font-size: 19px;
    font-weight: 400;
    line-height: 1.15;
    letter-spacing: 0.5px;
    text-transform: uppercase;
  }

  /* Front: black card, orange type */
  .card--front .card__email { color: var(--soft-grey); }
  .card--front .company { color: var(--accent); }
  .card--front .person__first { color: var(--soft-grey); }
  .card--front .person__last { color: var(--accent); }
  .card--front .address { color: var(--accent); }

  /* Back: yellow card, black type */
  .card--back .card__email { color: var(--ink); }
  .card--back .company { color: var(--ink); }
  .card--back .person__first { color: var(--ink-soft); }
  .card--back .person__last { color: var(--ink); }
  .card--back .address { color: var(--ink); }
</style>
</head>
<body>
<main class="sheet">
  <section class="card card--front">
    <p class="card__email">rmpcontracting@kestrelmail.com</p>
    <div class="card__details">
      <h1 class="company">RMP CONTRACTING</h1>
      <p class="person"><span class="person__first">Peter</span><span class="person__last">Langford</span></p>
      <p class="address">14 Calloway St<br>Eldon Vale<br>EV 6712<br>0487315962</p>
    </div>
  </section>

  <section class="card card--back">
    <p class="card__email">rmpcontracting@kestrelmail.com</p>
    <div class="card__details">
      <h2 class="company">RMP CONTRACTING</h2>
      <p class="person"><span class="person__first">Peter</span><span class="person__last">Langford</span></p>
      <p class="address">14 Calloway St<br>Eldon Vale<br>EV 6712<br>0487315962</p>
    </div>
  </section>
</main>
</body>
</html>
```